Constant Contact email marketing template

I need engaging customizable templates that can be used in multiple fundraising campaigns.

I included a school bus project that we used in a previous campaign. This campaign, however, is a $25 for $25 promotion. Consumers make a $25 contribution for the school or charity and receive back a $25 e-gift card to be used at area restaurants.

Important! This is a completely generic piece, capable of being used in schools, churches, or other civic organizations.

The 5 part example is NOT what I am looking for. I included it to suggest the concept. I am looking forward to viewing YOUR designs,

Target Market(s)

schools, leagues, nonprofit organizations

Font styles to use
Sans Serif

Colors

Designer to choose colors to be used in the design.

Requirements
Must have
• Must clearly present itself as a fundraising tool for schools, leagues and Nonprofit organizations.
• Must have 2 clickable buttons that allow member to click

```html
<!DOCTYPE html>
<html lang="en">
<head>
<meta charset="utf-8">
<title>Give $25, Get $25 Fundraiser</title>
<link rel="stylesheet" href="https://fonts.googleapis.com/css2?family=Kaushan+Script&family=Open+Sans:wght@700;800&family=Oswald:wght@300;400;500&display=swap">
<style>
  :root {
    --black: #0d0d0d;
    --green: #1f8a3c;
    --white: #ffffff;
    --gold: #f7b81a;
    --gold-light: #fbd24a;
    --red: #e0262b;
    --red-deep: #a8161b;
    --orange: #f0a635;
    --ink: #111111;
  }
  * { box-sizing: border-box; margin: 0; padding: 0; }
  html, body { width: 1200px; height: 2786px; overflow: hidden; background: var(--white); }
  .flyer { position: relative; width: 1200px; height: 2786px; overflow: hidden; background: var(--white); font-family: "Open Sans", sans-serif; }

  .backdrop { position: absolute; left: 0; top: 0; width: 1200px; height: 2786px; }

  .hero-photo { position: absolute; left: 359px; top: 80px; width: 1034px; height: 1034px; border-radius: 50%; border: 12px solid var(--white); background: radial-gradient(circle at 50% 45%, #e9e2d6 0%, #c9b9a3 45%, #f4f1ec 100%); }

  .masthead { position: absolute; z-index: 5; left: 0; top: 0; width: 1200px; height: 392px; background: var(--black); display: flex; align-items: center; justify-content: center; gap: 22px; padding-bottom: 40px; }
  .masthead__mark { width: 44px; height: 44px; background: var(--red-deep); }
  .masthead__name { font-weight: 800; font-size: 60px; color: var(--white); letter-spacing: 1px; }

  .badge { position: absolute; left: 53px; top: 796px; width: 538px; height: 538px; border-radius: 50%; border: 12px solid var(--white); background: radial-gradient(circle at 72% 40%, #8a8a8a 0%, #3a3a3a 45%, #111 100%); box-shadow: 0 10px 24px rgba(0,0,0,.35); text-align: center; color: var(--white); }
  .badge__top { position: absolute; top: 112px; left: 0; width: 100%; font-family: "Kaushan Script", cursive; font-size: 62px; }
  .badge__mid { position: absolute; top: 210px; left: 0; width: 100%; font-family: "Oswald", sans-serif; font-weight: 400; font-size: 52px; letter-spacing: 18px; padding-left: 18px; color: var(--orange); }
  .badge__bottom { position: absolute; top: 270px; left: 0; width: 100%; font-family: "Kaushan Script", cursive; font-size: 128px; }

  .bracket { position: absolute; left: 693px; top: 1218px; width: 130px; height: 470px; border: 5px solid var(--gold); border-right: none; border-radius: 8px 0 0 8px; }

  .coin { position: absolute; width: 350px; height: 350px; border-radius: 50%; background: radial-gradient(circle at 40% 35%, var(--gold-light) 0%, var(--gold) 60%, #e8a30c 100%); box-shadow: 0 10px 22px rgba(0,0,0,.35); text-align: center; color: var(--ink); }
  .coin--donate { left: 731px; top: 1073px; }
  .coin--card { left: 814px; top: 1397px; }
  .coin__script { position: absolute; left: 0; width: 100%; font-family: "Kaushan Script", cursive; font-size: 72px; color: var(--red); }
  .coin__small { position: absolute; left: 0; width: 100%; font-family: "Oswald", sans-serif; font-size: 20px; letter-spacing: 5px; color: var(--red); }
  .coin__amount { position: absolute; left: 0; width: 100%; font-family: "Oswald", sans-serif; font-weight: 500; font-size: 150px; line-height: 1; }
  .coin__amount sup { font-size: 72px; vertical-align: 30px; }

  .tagline { position: absolute; z-index: 2; left: 470px; top: 1480px; transform: rotate(-24deg); transform-origin: left top; font-family: "Kaushan Script", cursive; font-size: 124px; line-height: 0.92; color: var(--green); text-shadow: 0 5px 6px rgba(0,0,0,.3); white-space: nowrap; }
  .tagline span { display: block; }
  .tagline span:first-child { margin-left: 110px; }

  .cta { position: absolute; left: 0; width: 470px; height: 404px; border-radius: 0 240px 210px 0 / 0 210px 200px 0; text-decoration: none; }
  .cta--primary { top: 1682px; background: radial-gradient(circle at 60% 30%, #f25a2c 0%, var(--red) 45%, var(--red-deep) 100%); }
  .cta--upgrade { top: 2290px; background: radial-gradient(circle at 30% 40%, #f9d84a 0%, #efb225 50%, #c98a12 100%); }
  .cta__label { position: absolute; left: 160px; font-family: "Oswald", sans-serif; font-weight: 400; font-size: 36px; letter-spacing: 3px; white-space: nowrap; }
  .cta__price { position: absolute; left: 168px; font-family: "Oswald", sans-serif; font-weight: 300; font-size: 112px; line-height: 1; }
  .cta__price sup { font-size: 42px; vertical-align: 50px; font-weight: 400; }
  .cta__for { position: absolute; left: 132px; font-family: "Oswald", sans-serif; font-size: 22px; }
  .cta--primary .cta__label, .cta--primary .cta__for { color: var(--gold); }
  .cta--primary .cta__price { color: var(--white); }
  .cta--upgrade .cta__label, .cta--upgrade .cta__for, .cta--upgrade .cta__price { color: var(--red); }
  .play { position: absolute; left: 348px; width: 120px; height: 120px; }

  .pitch { position: absolute; left: 492px; top: 1790px; width: 650px; font-weight: 800; font-size: 46px; line-height: 56px; color: var(--ink); }

  .perks { position: absolute; left: 150px; top: 2094px; list-style: none; }
  .perks li { position: relative; padding-left: 54px; font-weight: 700; font-size: 29px; line-height: 49px; color: var(--red); white-space: nowrap; }
  .perks svg { position: absolute; left: 0; top: 8px; width: 34px; height: 32px; }

  .upgrade { position: absolute; left: 508px; top: 2346px; width: 440px; }
  .upgrade__title { font-weight: 800; font-size: 60px; color: var(--red); line-height: 1.1; }
  .upgrade__text { margin-top: 12px; font-weight: 800; font-size: 28px; line-height: 33px; color: var(--ink); }

  .contact { position: absolute; right: 32px; top: 2630px; list-style: none; }
  .contact li { display: flex; align-items: center; justify-content: flex-end; gap: 20px; height: 62px; font-weight: 800; font-size: 29px; color: var(--white); }
  .contact svg { width: 50px; height: 50px; }
</style>
</head>
<body>
<main class="flyer">

  <svg class="backdrop" viewBox="0 0 1200 2786" aria-hidden="true">
    <rect x="0" y="0" width="1200" height="2786" fill="var(--green)"/>
    <circle cx="876" cy="600" r="780" fill="var(--black)"/>
    <circle cx="876" cy="600" r="640" fill="var(--green)"/>
    <path d="M0 1660 C250 1500 520 1400 820 1378 C980 1366 1100 1330 1200 1300 V2786 H0 Z" fill="var(--white)"/>
    <path d="M1200 2360 V2786 H500 C760 2640 1000 2480 1200 2360 Z" fill="var(--green)"/>
  </svg>

  <div class="hero-photo" role="img" aria-label="Photo of a cheering group of people with raised arms"></div>

  <header class="masthead">
    <span class="masthead__mark"></span>
    <span class="masthead__name">BROOKFIELD SCHOOLS</span>
  </header>

  <div class="badge">
    <div class="badge__top">greatest</div>
    <div class="badge__mid">FUNDRAISER</div>
    <div class="badge__bottom">ever!</div>
  </div>

  <div class="bracket"></div>

  <div class="coin coin--donate">
    <div class="coin__script" style="top:40px">donate</div>
    <div class="coin__amount" style="top:140px"><sup>$</sup>25</div>
  </div>

  <div class="coin coin--card">
    <div class="coin__script" style="top:26px">e-Gift</div>
    <div class="coin__small" style="top:122px">CARD</div>
    <div class="coin__amount" style="top:160px"><sup>$</sup>25</div>
  </div>

  <div class="tagline"><span>and</span><span>you get</span></div>

  <a class="cta cta--primary" href="#give-25">
    <span class="cta__label" style="top:58px">CLIK HERE</span>
    <span class="cta__price" style="top:104px"><sup>$</sup>25</span>
    <span class="cta__for" style="top:200px">FOR</span>
    <span class="cta__price" style="top:222px"><sup>$</sup>25</span>
    <svg class="play" style="top:20px" viewBox="0 0 124 124" aria-hidden="true">
      <circle cx="62" cy="62" r="58" fill="#f2f2f2" stroke="#bbb" stroke-width="3"/>
      <circle cx="62" cy="62" r="44" fill="var(--red)"/>
      <path d="M50 40 L86 62 L50 84 Z" fill="var(--white)"/>
    </svg>
  </a>

  <p class="pitch">Simply donate $25 and<br>we give you $25 back in<br>e-Gift Cards for<br>restaurants in your area!</p>

  <ul class="perks">
    <li><svg viewBox="0 0 34 32"><path d="M3 17 L13 27 L31 4" fill="none" stroke="var(--red)" stroke-width="6" stroke-linecap="round" stroke-linejoin="round"/></svg>More than 500,000 deals available every day</li>
    <li><svg viewBox="0 0 34 32"><path d="M3 17 L13 27 L31 4" fill="none" stroke="var(--red)" stroke-width="6" stroke-linecap="round" stroke-linejoin="round"/></svg>Local independent neughborhood restaurants</li>
    <li><svg viewBox="0 0 34 32"><path d="M3 17 L13 27 L31 4" fill="none" stroke="var(--red)" stroke-width="6" stroke-linecap="round" stroke-linejoin="round"/></svg>Always available. Never expire.</li>
    <li><svg viewBox="0 0 34 32"><path d="M3 17 L13 27 L31 4" fill="none" stroke="var(--red)" stroke-width="6" stroke-linecap="round" stroke-linejoin="round"/></svg>More than 62,000+ restaurants &amp; providers nationwide</li>
  </ul>

  <a class="cta cta--upgrade" href="#give-30">
    <span class="cta__label" style="top:72px">CLIK HERE</span>
    <span class="cta__price" style="top:122px"><sup>$</sup>30</span>
    <span class="cta__for" style="top:218px">FOR</span>
    <span class="cta__price" style="top:240px"><sup>$</sup>50</span>
    <svg class="play" style="top:48px" viewBox="0 0 124 124" aria-hidden="true">
      <circle cx="62" cy="62" r="58" fill="#f2f2f2" stroke="#bbb" stroke-width="3"/>
      <circle cx="62" cy="62" r="44" fill="#e8a91c"/>
      <path d="M50 40 L86 62 L50 84 Z" fill="var(--white)"/>
    </svg>
  </a>

  <div class="upgrade">
    <h2 class="upgrade__title">$30 for $50</h2>
    <p class="upgrade__text">For only an extra $5 we<br>will send you an additio-<br>nal $25 e-Gift Card.</p>
  </div>

  <ul class="contact">
    <li>www.dinegive.org
      <svg viewBox="0 0 50 50" aria-hidden="true"><circle cx="25" cy="25" r="22" fill="none" stroke="var(--white)" stroke-width="4"/><path d="M13 26 L25 15 L37 26 M17 24 V35 H33 V24" fill="none" stroke="var(--white)" stroke-width="3.5" stroke-linejoin="round"/></svg>
    </li>
    <li>support@dinegive.org
      <svg viewBox="0 0 50 50" aria-hidden="true"><circle cx="25" cy="25" r="22" fill="none" stroke="var(--white)" stroke-width="4"/><rect x="14" y="17" width="22" height="16" rx="2" fill="var(--white)"/><path d="M14 18 L25 27 L36 18" fill="none" stroke="var(--green)" stroke-width="2.5"/></svg>
    </li>
  </ul>

</main>
</body>
</html>
```